TORNAVE5 Research Outcomes (e-Toolkit)

I would like you to design an electronic document that can be used to display the outcomes of the TORNAVE5 Research that can easily be downloaded from a website. This document will help nurses, educators, students and their supervisors to be able to better understand the outcomes of the research and apply it to their own practice. It should be something they can print out (A4 size) and refer to easily. It should be quite graphical and represent male and female nurses working in different specialty areas (emergency, primary healthcare, aged care, etc.), across hospital to primary healthcare (community) contexts. It should be professional, clean and crisp in appearance. There are areas in yellow in the attached document that are yet to be determined. All images within the document can be amended to better reflect the design of the document and the intent of its contained content. An example of the type of document I'm looking for is attached as "standards.pdf". It should be approximately 15 pages in length.
Updates

The project does not have to use the TORNAVE5 logo or its colours as a main design feature of the project.

Target Market(s)

Nurses, educators and students.

Industry/Entity Type

Education

Font styles to use
Sans Serif

Colors

Designer to choose colors to be used in the design.

Requirements
Must have
• Must have a diagram depicting the interrelatedness of all the individual metaspecialties. The contained diagrams can be modified to suit graphic design needs.
• Images of nursing professionals should appear Australian.
Nice to have
• I would like them to try and re-configure the diagrams as they are boring and I hate the colours. Images of collaboration amongst different healthcare team members would be nice.
Should not have
• Only images of female nurses or only images (if chosen) of nurses only working in a hospital.

```html
<!DOCTYPE html>
<html lang="en">
<head>
<meta charset="UTF-8">
<title>Australian Nurse Practitioner Clinical Specialty Learning and Capability</title>
<link rel="stylesheet" href="https://fonts.googleapis.com/css2?family=Roboto+Condensed:wght@400;700&display=swap">
<style>
  :root {
    --green-deep: #2fb862;
    --green-mid: #45c771;
    --green-light: #7fdc9f;
    --white: #ffffff;
    --purple: #7a2fb8;
    --author-grey: #6d6d6d;
    --page: #ffffff;
  }
  * { margin: 0; padding: 0; box-sizing: border-box; }
  html, body {
    width: 847px;
    height: 1200px;
    overflow: hidden;
    background: var(--page);
  }
  .cover {
    position: relative;
    width: 847px;
    height: 1200px;
    background: var(--page);
    font-family: "Roboto Condensed", Arial, sans-serif;
  }
  .hero {
    position: absolute;
    left: 0; top: 0;
    width: 847px;
    height: 705px;
    background:
      radial-gradient(ellipse at 78% 18%, rgba(255,255,255,0.22), transparent 45%),
      radial-gradient(ellipse at 22% 80%, rgba(255,255,255,0.14), transparent 50%),
      linear-gradient(160deg, var(--green-light) 0%, var(--green-mid) 45%, var(--green-deep) 100%);
  }
  .title {
    position: absolute;
    left: 0;
    top: 372px;
    width: 847px;
    text-align: center;
    color: var(--white);
    font-weight: 700;
    font-size: 37px;
    line-height: 50px;
    letter-spacing: 0.3px;
    text-transform: uppercase;
  }
  .brand {
    position: absolute;
    left: 0;
    top: 790px;
    width: 847px;
    display: flex;
    justify-content: center;
    align-items: center;
    gap: 16px;
  }
  .brand-mark {
    width: 38px;
    height: 38px;
    background: var(--green-mid);
  }
  .brand-name {
    color: var(--purple);
    font-weight: 700;
    font-size: 52px;
    letter-spacing: 1px;
  }
  .authors {
    position: absolute;
    left: 0;
    top: 950px;
    width: 847px;
    text-align: center;
    color: var(--author-grey);
    font-size: 18px;
    line-height: 25px;
    list-style: none;
  }
  .footer-band {
    position: absolute;
    left: 0;
    bottom: 0;
    width: 847px;
    height: 40px;
    background: var(--purple);
  }
</style>
</head>
<body>
  <main class="cover">
    <div class="hero" role="img" aria-label="Green-tinted photograph of a nurse practitioner caring for a patient in a hospital bed"></div>

    <h1 class="title">
      Australian Nurse Practitioner<br>
      Clinical Specialty Learning<br>
      and Capability
    </h1>

    <div class="brand">
      <span class="brand-mark"></span>
      <span class="brand-name">TORNAVE5</span>
    </div>

    <ul class="authors">
      <li>Authors:</li>
      <li>Dr Ruth Calloway, RN PhD HFACNP xx</li>
      <li>Professor Emeritus Alan Prewitt RN PhD HFACNP xx</li>
      <li>Professor Megan Lindqvist, RN PHD xx</li>
      <li>Ms Karen Whitlow RN NP xx HFACNP</li>
      <li>Dr Daniel Ostrander RN NP PhD xx HFACNP</li>
    </ul>

    <div class="footer-band"></div>
  </main>
</body>
</html>
```